High Quality fast food restaurant - Tomanyo

Tomanyo is a fast food company with its target's focused on logistic, simplicity, high quality, freshness and modern.

We need a web design where the customers can get a complete idea of our high quality completeness, we want to take fast food to a new upper level.

We would like to see the colours of wood and metal. Pictures have been attached of our local.

We would like to have something in similar to: http://www.qpz.example/
Updates

Images for the food we are going to sell can be found here: http://shrt.example/uWQa7

It will be the images with rice, french fries or pita bread.

Target Market(s)

The fast food eating people between sloppy food and restaurant level.

Industry/Entity Type

Fast Food Restaurant

Requirements
Should not have
• No Flash or Java

```html
<!DOCTYPE html>
<html lang="en">
<head>
<meta charset="utf-8">
<title>Tomanyo – High Quality Fast Food</title>
<link rel="stylesheet" href="https://fonts.googleapis.com/css2?family=Oswald:wght@400;500;700&family=Pacifico&family=Noto+Sans:wght@400&display=swap">
<style>
  :root {
    --bar-dark: #2a140d;
    --bar-mid: #3a1d12;
    --wood-dark: #2b1109;
    --wood-mid: #5a2614;
    --wood-light: #7a3a1c;
    --table: #8a3e14;
    --table-light: #a85a26;
    --cream: #fbf1e1;
    --cream-deep: #f1dfc0;
    --accent: #f04a2a;
    --ink: #1e0e08;
    --white: #ffffff;
  }
  * { box-sizing: border-box; margin: 0; padding: 0; }
  html, body { width: 1200px; height: 1089px; overflow: hidden; }
  body {
    position: relative;
    background: radial-gradient(ellipse at 30% 10%, #fff8ec 0%, var(--cream) 40%, var(--cream-deep) 100%);
    font-family: "Noto Sans", Verdana, sans-serif;
    color: var(--ink);
  }
  .brand {
    position: absolute;
    font-family: "Oswald", sans-serif;
    font-weight: 700;
    color: var(--white);
    letter-spacing: 1px;
    line-height: 1;
  }
  .nav {
    position: absolute;
    display: flex;
    list-style: none;
    font-family: "Oswald", sans-serif;
    font-size: 14px;
    color: var(--white);
  }
  .nav li { margin-left: 0; }
  .nav li + li { margin-left: 41px; }

  .top-bar {
    position: absolute; left: 0; top: 0; width: 1200px; height: 48px;
    background: linear-gradient(var(--bar-mid), var(--bar-dark));
    border-bottom: 1px solid #140805;
  }
  .top-bar .brand { left: 148px; top: 8px; font-size: 40px; background: #1c0c07; padding: 2px 8px; }
  .top-bar .nav { left: 657px; top: 16px; }

  .hero {
    position: absolute; left: 0; top: 48px; width: 1200px; height: 388px;
    background:
      repeating-linear-gradient(90deg, rgba(0,0,0,0.18) 0 2px, transparent 2px 34px),
      radial-gradient(ellipse at 50% 30%, var(--wood-light) 0%, var(--wood-mid) 45%, var(--wood-dark) 100%);
    overflow: hidden;
  }
  .hero .table {
    position: absolute; left: 0; top: 318px; width: 1200px; height: 70px;
    background:
      repeating-linear-gradient(0deg, rgba(0,0,0,0.12) 0 1px, transparent 1px 7px),
      linear-gradient(var(--table-light), var(--table) 40%, #6a2c0c);
  }
  .script { font-family: "Pacifico", cursive; position: absolute; }
  .hero .with-fries { left: 229px; top: 110px; font-size: 26px; color: var(--white); }
  .hero .and-salad { left: 864px; top: 110px; font-size: 26px; color: var(--white); }
  .hero .tagline { left: 518px; top: 48px; font-size: 27px; color: var(--accent); }
  .hero .title {
    position: absolute; left: 474px; top: 94px;
    font-family: "Oswald", sans-serif; font-weight: 500; font-size: 33px;
    color: var(--white); letter-spacing: 0.5px;
  }
  .food { position: absolute; }
  .food.fries { left: 152px; top: 180px; width: 290px; height: 170px; border-radius: 50% 50% 46% 46%;
    background: radial-gradient(ellipse at 50% 40%, #f7c448 0%, #e4a12c 55%, #e9e2d3 80%); }
  .food.kebab { left: 426px; top: 182px; width: 370px; height: 190px; border-radius: 44% 44% 48% 48%;
    background: radial-gradient(ellipse at 50% 55%, #7a4430 0%, #b96b48 35%, #e8dcc4 70%); }
  .food.salad { left: 784px; top: 160px; width: 290px; height: 195px; border-radius: 40% 40% 50% 50%;
    background: linear-gradient(#5f9a2a 0%, #78b23a 35%, #f4f4f2 55%, #e2e2e0 100%); }

  .section-title { position: absolute; font-family: "Pacifico", cursive; font-size: 27px; line-height: 1.2; }
  .section-title .lead { color: var(--accent); }
  .welcome-title { left: 139px; top: 512px; }
  .contact-title { left: 786px; top: 512px; }

  .welcome-text {
    position: absolute; left: 147px; top: 582px; width: 540px;
    font-size: 13.5px; line-height: 17px;
  }
  .welcome-text p + p { margin-top: 17px; }

  .gallery .photo { position: absolute; top: 782px; width: 162px; height: 121px; }
  .photo.shopfront { left: 142px; background: linear-gradient(135deg, #3f8a78, #5a3526 55%, #2b1a12); }
  .photo.wrap { left: 323px; background: linear-gradient(135deg, #7a5238, #e8e0cc 45%, #4f8a3a 70%, #6b3f26); }
  .photo.chicken { left: 502px; background: radial-gradient(ellipse at 50% 40%, #6a3818, #a4622e 55%, #d9cba6); }

  .contact-details { position: absolute; left: 791px; top: 584px; font-size: 13.5px; line-height: 17px; width: 240px; }
  .contact-details dt { color: var(--accent); }
  .contact-details dd + dt { margin-top: 17px; }

  .map { position: absolute; left: 786px; top: 720px; width: 252px; height: 200px;
    background: linear-gradient(135deg, #e9e6df 0%, #dcd8cf 50%, #cfe0c0 100%); }

  .footer {
    position: absolute; left: 0; top: 973px; width: 1200px; height: 116px;
    background:
      repeating-linear-gradient(90deg, rgba(0,0,0,0.15) 0 2px, transparent 2px 40px),
      linear-gradient(#2e150c, #22100a);
  }
  .footer .brand { left: 163px; top: 27px; font-size: 38px; }
  .footer .nav { left: 653px; top: 21px; }
</style>
</head>
<body>
  <header class="top-bar">
    <div class="brand">TOMANYO</div>
    <ul class="nav">
      <li>Home</li><li>Menu</li><li>Locations</li><li>Gift Cards</li><li>Contact Us</li>
    </ul>
  </header>

  <section class="hero">
    <div class="table"></div>
    <div class="food fries" role="img" aria-label="Plate of crinkle-cut french fries"></div>
    <div class="food kebab" role="img" aria-label="Pita bread kebab with meat, tomato and onion"></div>
    <div class="food salad" role="img" aria-label="White bowl of fresh green salad"></div>
    <div class="script with-fries">with fries</div>
    <div class="script tagline">Tasty &amp; Fresh</div>
    <h1 class="title">PITA BREAD KEBAB</h1>
    <div class="script and-salad">and salad</div>
  </section>

  <h2 class="section-title welcome-title"><span class="lead">Welcome to</span> Tomanyo</h2>
  <div class="welcome-text">
    <p>Lorem ipsum dolor sit amet, eam in meis dolore salutatus, te nec ignota indoctum, utamur vidisse recteque vis no. Pri elitr nostrum interesset at, id eam molestie gubergren honestatis, ei ius aperiam hendrerit. Volutpat reprehendunt eam te, vis expetendis sententiae sadipscing ad, ne torquatos efficiantur vis. Has no omnes electram. Ad elitr homero tacimates sed.</p>
    <p>Te quo movet quaeque deleniti, pri ei splendide dissentiet. Sed aeque nonumy cu, pro te liber paulo dolorem. Partiendo expetendis comprehensam cu ius. Vide bonorum ne qui.</p>
  </div>
  <div class="gallery">
    <div class="photo shopfront" role="img" aria-label="Restaurant shopfront"></div>
    <div class="photo wrap" role="img" aria-label="Kebab wrap with salad"></div>
    <div class="photo chicken" role="img" aria-label="Grilled chicken on rice"></div>
  </div>

  <h2 class="section-title contact-title"><span class="lead">Contact</span> Us</h2>
  <dl class="contact-details">
    <dt>Address:</dt>
    <dd>14 Harlow Lane, Brenwick Heights, VIC, 3999</dd>
    <dt>Phone Number:</dt>
    <dd>03 5550 1842</dd>
  </dl>
  <div class="map" role="img" aria-label="Street map showing the restaurant location"></div>

  <footer class="footer">
    <div class="brand">TOMANYO</div>
    <ul class="nav">
      <li>Home</li><li>Menu</li><li>Locations</li><li>Gift Cards</li><li>Contact Us</li>
    </ul>
  </footer>
</body>
</html>
```